Letterhead - Quarrington Law Group

I receive a fantastic logo from you guys and I'd like to incorporate it into business cards and letterhead. I accidentally approved design No. 32361474 and contacted designer Ravindra, and Ravindra sent me the zip folder for Design No. 32361417, which I very much appreciate.
I'd like to order business cards and letterhead with Design No. 32361417 as soon as possible, but I want to make sure that you incorporate the correct design (attached). I'd also like to provide my information to add (address, phone number, email, fax) but I'm not quite sure how to do it.
The information that I would like on the business cards and letterhead is as follows:
Quarrington Law Group
Theodore K. Quarrington, Esq.
2741 Hollis Avenue, Suite 520
San Francisco, CA 94087
Office: (415) 378-6130
Fax: (415) 746-0183
ted@quarringtonlawgroup-example.com
Thanks in advance for any guidance.
Ted Quarrington
Quarrington Law Group
(415) 831-4497 (cell)

```html
<!DOCTYPE html>
<html lang="en">
<head>
<meta charset="utf-8">
<title>Quarrington Law Group — Stationery</title>
<link href="https://fonts.googleapis.com/css2?family=Open+Sans:wght@400&family=Roboto:wght@400;500&display=swap" rel="stylesheet">
<style>
  :root {
    --backdrop: #5d5c6a;
    --paper: #f1f1f3;
    --paper-shade: #e6e6ea;
    --flap: #141313;
    --ink: #1b1b1d;
    --ink-soft: #4a4a50;
    --fold: #d4d4da;
    --signature: #c9ccd6;
  }
  * { margin: 0; padding: 0; box-sizing: border-box; }
  html, body { width: 1200px; height: 1050px; overflow: hidden; }
  body {
    background: var(--backdrop);
    position: relative;
    font-family: "Roboto", Arial, sans-serif;
    color: var(--ink);
  }
  .envelope { position: absolute; }
  .envelope svg { display: block; }
  .flap-name {
    position: absolute; left: 0; right: 0;
    text-align: center; color: #ffffff;
    font-family: "Roboto", Arial, sans-serif; font-weight: 400;
    font-size: 13px; letter-spacing: 1.5px;
  }
  .envelope-front { left: 196px; top: 239px; width: 421px; height: 293px; }
  .envelope-front .flap-name { top: 34px; }
  .return-address {
    position: absolute; left: 26px; top: 233px;
    font-size: 7.2px; line-height: 8.6px; color: var(--ink-soft);
  }
  .return-address .firm { font-weight: 500; color: var(--ink); }
  .envelope-back { left: 195px; top: 568px; width: 419px; height: 210px; }
  .envelope-back .flap-name { top: 32px; }

  .letterhead {
    position: absolute; left: 662px; top: 250px;
    width: 405px; height: 540px; background: var(--paper);
  }
  .brand {
    position: absolute; left: 40px; top: 36px;
    display: flex; align-items: center; gap: 6px;
  }
  .brand-square { width: 12px; height: 12px; background: var(--flap); }
  .brand-name { font-size: 10px; font-weight: 400; color: var(--ink); letter-spacing: 0.6px; }
  .contact {
    position: absolute; right: 22px; top: 34px;
    font-size: 7.4px; line-height: 9.4px; color: var(--ink-soft);
  }
  .contact b { font-weight: 500; color: var(--ink); }
  .letter-body {
    position: absolute; left: 42px; top: 137px; width: 323px;
    font-family: "Open Sans", Arial, sans-serif;
    font-size: 6.5px; line-height: 10.2px; color: var(--ink-soft);
  }
  .letter-body p { text-align: justify; margin-bottom: 10.2px; }
  .letter-body .salutation { margin-bottom: 10.2px; }
  .signature {
    position: absolute; left: 42px; top: 410px;
    width: 46px; height: 38px; background: var(--signature); opacity: .6;
  }
  .letter-footer {
    position: absolute; left: 0; right: 0; top: 500px;
    text-align: center; font-size: 7px; line-height: 9px; color: var(--ink-soft);
  }
  .letter-footer b { font-weight: 500; color: var(--ink); }
</style>
</head>
<body>

  <div class="envelope envelope-front">
    <svg width="421" height="293" viewBox="0 0 421 293" aria-hidden="true">
      <rect x="0" y="84" width="421" height="209" fill="var(--paper)"/>
      <path d="M0 84 L28 8 Q31 0 40 0 L381 0 Q390 0 393 8 L421 84 Z" fill="var(--flap)"/>
    </svg>
    <div class="flap-name">QUARRINGTON LAW GROUP</div>
    <div class="return-address">
      <div class="firm">Quarrington Law Group</div>
      <div>Theodore K. Quarrington, Esq.</div>
      <div>2741 Hollis Avenue, Suite 520</div>
      <div>San Francisco, CA 94087</div>
    </div>
  </div>

  <div class="envelope envelope-back">
    <svg width="419" height="210" viewBox="0 0 419 210" aria-hidden="true">
      <rect x="0" y="0" width="419" height="210" fill="var(--paper)"/>
      <path d="M0 210 L40 86 M419 210 L379 86" stroke="var(--fold)" stroke-width="1" fill="none"/>
      <path d="M0 0 L419 0 L390 78 Q386 86 376 86 L43 86 Q33 86 29 78 Z" fill="var(--flap)"/>
    </svg>
    <div class="flap-name">QUARRINGTON LAW GROUP</div>
  </div>

  <div class="letterhead">
    <div class="brand">
      <span class="brand-square"></span>
      <span class="brand-name">QUARRINGTON LAW GROUP</span>
    </div>
    <div class="contact">
      <div><b>Office :</b> (415) 378-6130</div>
      <div><b>Cell :</b> (415) 831-4497</div>
      <div><b>Fax :</b> (415) 746-0183</div>
      <div>ted@quarringtonlawgroup-example.com</div>
    </div>
    <div class="letter-body">
      <div class="salutation">Dear customer,</div>
      <p>Lorem ipsum dolor sit amet, consectetur adipisicing elit, sed do eiusmod tempor incididunt ut labore et dolore magna aliqua. Ut enim ad minim veniam, quis nostrud exercitation ullamco laboris nisi ut aliquip ex ea commodo consequat. Duis aute irure dolor in reprehenderit in voluptate velit esse cillum dolore eu fugiat nulla pariatur. Excepteur sint occaecat cupidatat non proident, sunt in culpa qui officia deserunt mollit anim id est laborum.</p>
      <p>Lorem ipsum dolor sit amet, consectetur adipisicing elit, sed do eiusmod tempor incididunt ut labore et dolore magna aliqua. Ut enim ad minim veniam, quis nostrud exercitation ullamco laboris nisi ut aliquip ex ea commodo consequat. Duis aute irure dolor in reprehenderit in voluptate velit esse cillum dolore eu fugiat nulla pariatur. Excepteur sint occaecat cupidatat non proident, sunt in culpa qui officia deserunt mollit anim id est laborum.</p>
      <p>Lorem ipsum dolor sit amet, consectetur adipisicing elit, sed do eiusmod tempor incididunt ut labore et dolore magna aliqua. Ut enim ad minim veniam, quis nostrud exercitation ullamco laboris nisi ut aliquip ex ea commodo consequat. Duis aute irure dolor in reprehenderit in voluptate velit esse cillum dolore eu fugiat nulla pariatur. Excepteur sint occaecat cupidatat non proident, sunt in culpa qui officia deserunt mollit anim id est laborum.</p>
      <p>Lorem ipsum dolor sit amet, consectetur adipisicing elit, sed do eiusmod tempor incididunt ut labore et dolore magna aliqua. Ut enim ad minim veniam, quis nostrud exercitation ullamco laboris nisi ut aliquip ex ea commodo consequat. Duis aute irure dolor in reprehenderit.</p>
      <div>Yours Sincerely,</div>
    </div>
    <div class="signature" role="img" aria-label="Handwritten signature"></div>
    <div class="letter-footer">
      <div><b>Quarrington Law Group</b></div>
      <div>Theodore K. Quarrington, Esq. 2741 Hollis Avenue, Suite 520 San Francisco, CA 94087</div>
    </div>
  </div>

</body>
</html>
```